Tea company needs a bottle label Design

Attached are some examples im looking for however please send me an email at minrota@vellufo.com for design specs.

Font styles to use
Serif

Requirements
Must have
• We want a metallic gold coloring see below also the background will be a matte white.
• For the Turtle add a slight texture so its embossed gold.
• Have the Turtle positioned up top
• Below that have it say "Premium Gold Extract" under that add "Maeng Da"
• Add a ribbon with our title "Vellufo Running down" with "15 ML on the end of the ribbon.
• Have dots going across the bottle and in the middle put "Mitragyna Speciosa"
• On the Side panels: Please include this warning "Any statements made have not been evaluated by the Remedy & Tonic Bureau. All information provided is strictly for informational purposes and according to botanical research. While Kratom (Mitragyna Speciosa) is recognized in many cultures, U.S. Remedy and Tonic Bureau (RTB) strictly prohibits internal use of this herb. Do not use if you are pregnant or may become pregnant, or if you’re breastfeeding. Keep out of the reach of children."
• On the other side panel: Please copy this info below just remove the word powder from the paragraph.

```html
<!DOCTYPE html>
<html lang="en">
<head>
<meta charset="utf-8">
<title>Vellufo Premium Gold Extract – Bottle Label</title>
<link rel="stylesheet" href="https://fonts.googleapis.com/css2?family=Crimson+Pro:wght@600;700&family=Barlow:wght@500;600&display=swap">
<style>
  :root {
    --backdrop: #c8c8c8;
    --label-white: #f7f7f5;
    --gold-deep: #8a5a28;
    --gold-mid: #b9824a;
    --gold-light: #e2c49d;
    --gold-text: #9c6a36;
    --ribbon-text: #f4ece2;
  }
  * { box-sizing: border-box; margin: 0; padding: 0; }
  html, body {
    width: 887px;
    height: 1200px;
    overflow: hidden;
    background: var(--backdrop);
  }
  .canvas {
    position: relative;
    width: 887px;
    height: 1200px;
  }
  .label {
    position: absolute;
    left: 202px;
    top: 385px;
    width: 468px;
    height: 600px;
    background: var(--label-white);
    box-shadow: 0 2px 10px rgba(0,0,0,0.08);
  }
  .metallic {
    background: linear-gradient(180deg, var(--gold-light) 0%, var(--gold-mid) 45%, var(--gold-deep) 100%);
    -webkit-background-clip: text;
    background-clip: text;
    color: transparent;
  }
  .brand-mark {
    position: absolute;
    left: 0;
    top: 88px;
    width: 306px;
    display: flex;
    align-items: center;
    justify-content: center;
    gap: 10px;
  }
  .brand-mark__dot {
    width: 22px;
    height: 22px;
    border-radius: 50%;
    background: var(--gold-mid);
  }
  .brand-mark__name {
    font-family: "Crimson Pro", serif;
    font-weight: 700;
    font-size: 34px;
    color: var(--gold-mid);
    letter-spacing: 1px;
  }
  .title-premium {
    position: absolute;
    left: 58px;
    top: 212px;
    width: 210px;
    text-align: center;
    font-family: "Crimson Pro", serif;
    font-weight: 600;
    font-size: 42px;
    letter-spacing: 0.5px;
    line-height: 1;
  }
  .title-extract {
    position: absolute;
    left: 18px;
    top: 287px;
    font-family: "Barlow", sans-serif;
    font-weight: 600;
    font-size: 55px;
    line-height: 1;
    letter-spacing: -0.5px;
  }
  .title-strain {
    position: absolute;
    left: 88px;
    top: 388px;
    font-family: "Crimson Pro", serif;
    font-weight: 700;
    font-size: 29px;
    color: var(--gold-text);
    line-height: 1;
  }
  .ribbon {
    position: absolute;
    left: 373px;
    top: 10px;
    width: 38px;
    height: 330px;
    background: linear-gradient(90deg, var(--gold-deep), var(--gold-light) 50%, var(--gold-mid));
    display: flex;
    align-items: center;
    justify-content: center;
  }
  .ribbon__name {
    writing-mode: vertical-rl;
    font-family: "Crimson Pro", serif;
    font-weight: 700;
    font-size: 34px;
    letter-spacing: 6px;
    color: var(--ribbon-text);
  }
  .volume {
    position: absolute;
    left: 375px;
    top: 348px;
    font-family: "Barlow", sans-serif;
    font-weight: 500;
    font-size: 21px;
    color: var(--gold-text);
  }
  .dot-band {
    position: absolute;
    left: 0;
    top: 453px;
    width: 100%;
    height: 67px;
  }
  .dot-band__tone {
    position: absolute;
    inset: 0;
    background: linear-gradient(180deg, rgba(201,170,135,0) 0%, rgba(201,170,135,0.55) 50%, rgba(201,170,135,0) 100%);
  }
  .dot-band__text {
    position: absolute;
    left: 40px;
    top: 22px;
    font-family: "Barlow", sans-serif;
    font-weight: 500;
    font-size: 21px;
    color: var(--gold-deep);
  }
</style>
</head>
<body>
  <main class="canvas">
    <section class="label">
      <div class="brand-mark">
        <span class="brand-mark__dot"></span>
        <span class="brand-mark__name">Vellufo</span>
      </div>

      <h1 class="title-premium metallic">PREMIUM</h1>
      <h2 class="title-extract metallic">Gold Extract</h2>
      <p class="title-strain">Maeng Da</p>

      <div class="ribbon">
        <span class="ribbon__name">VELLUFO</span>
      </div>
      <p class="volume">15mL</p>

      <div class="dot-band">
        <div class="dot-band__tone" role="img" aria-label="Band of fine gold halftone dots running across the label"></div>
        <p class="dot-band__text">Mitragyna Speciosa</p>
      </div>
    </section>
  </main>
</body>
</html>
```